22nd Annual Pacific Lantern Cinema Showcase POSTER

Need a modern stylish chic poster for PLCS's 22nd film festival. Must appeal to our upscale audience and interest new attendees.
Dates are August 23 - 30th, 2019 www.plcs-showcase.example

Target Market(s)

we demo flyer attached

Industry/Entity Type

Film Production

Colors

Designer to choose colors to be used in the design.

Requirements
Must have
• Modern, chic, stylish - EYE catching
Nice to have
• Obscure - different - something new
Should not have
• NO CLIP ART

```html
<!DOCTYPE html>
<html lang="en">
<head>
<meta charset="utf-8">
<title>Pacific Lantern Cinema Showcase — Poster</title>
<link rel="stylesheet" href="https://fonts.googleapis.com/css2?family=Bodoni+Moda:opsz,wght@6..96,500;6..96,600;6..96,700&display=swap">
<style>
  :root {
    --backdrop: #c9c9c9;
    --poster-black: #0e0e0e;
    --ink-white: #ffffff;
    --photo-edge: #1b128a;
    --photo-deep: #2d20c4;
    --photo-violet: #7a2fe0;
    --photo-magenta: #c04ce8;
    --photo-mist: #d9ccf7;
  }
  html, body {
    margin: 0;
    padding: 0;
    width: 1200px;
    height: 1000px;
    overflow: hidden;
    background: var(--backdrop);
  }
  .stage {
    position: relative;
    width: 1200px;
    height: 1000px;
  }
  .poster {
    position: absolute;
    top: 153px;
    width: 560px;
    height: 718px;
  }
  .poster--classic { left: 33px; }
  .poster--seal { left: 619px; }
  .poster-art { display: block; width: 560px; height: 718px; }
  .sheet { fill: var(--poster-black); }
  .display-type {
    font-family: "Bodoni Moda", "Didot", serif;
    font-weight: 600;
    fill: var(--ink-white);
  }
  .info-type {
    font-family: "Bodoni Moda", "Didot", serif;
    font-weight: 700;
    fill: var(--ink-white);
  }
  .seal-type {
    font-family: "Bodoni Moda", "Didot", serif;
    font-weight: 700;
    fill: var(--ink-white);
  }
  .brand-name {
    font-family: "Bodoni Moda", "Didot", serif;
    font-weight: 700;
    fill: var(--ink-white);
  }
  .brand-mark { fill: none; stroke: var(--ink-white); stroke-width: 1.5; }
</style>
</head>
<body>
<main class="stage">

  <svg width="0" height="0" style="position:absolute" aria-hidden="true">
    <defs>
      <linearGradient id="photo-base" x1="0" y1="0" x2="0" y2="1">
        <stop offset="0" stop-color="var(--photo-edge)"/>
        <stop offset="0.45" stop-color="var(--photo-deep)"/>
        <stop offset="0.78" stop-color="#3a27d0"/>
        <stop offset="1" stop-color="#6a58e0"/>
      </linearGradient>
      <radialGradient id="photo-spot" cx="0.5" cy="0.5" r="0.5">
        <stop offset="0" stop-color="var(--photo-magenta)" stop-opacity="0.95"/>
        <stop offset="0.55" stop-color="var(--photo-violet)" stop-opacity="0.6"/>
        <stop offset="1" stop-color="var(--photo-violet)" stop-opacity="0"/>
      </radialGradient>
      <radialGradient id="photo-floor" cx="0.5" cy="0.5" r="0.5">
        <stop offset="0" stop-color="var(--photo-mist)" stop-opacity="0.95"/>
        <stop offset="1" stop-color="var(--photo-mist)" stop-opacity="0"/>
      </radialGradient>
      <radialGradient id="photo-vignette" cx="0.5" cy="0.45" r="0.75">
        <stop offset="0.55" stop-color="#0a0640" stop-opacity="0"/>
        <stop offset="1" stop-color="#0a0640" stop-opacity="0.55"/>
      </radialGradient>
      <filter id="photo-soften" x="-30%" y="-30%" width="160%" height="160%">
        <feGaussianBlur stdDeviation="18"/>
      </filter>
      <clipPath id="photo-frame"><rect x="104" y="102" width="356" height="507"/></clipPath>
    </defs>
  </svg>

  <!-- Variant with stacked festival details -->
  <article class="poster poster--classic">
    <svg class="poster-art" viewBox="0 0 560 718" xmlns="http://www.w3.org/2000/svg">
      <rect class="sheet" width="560" height="718"/>

      <g class="feature-photo" role="img" aria-label="Photograph of a classical plaster bust wearing 3D cinema glasses, lit in magenta and violet against a deep blue studio backdrop" clip-path="url(#photo-frame)">
        <rect x="104" y="102" width="356" height="507" fill="url(#photo-base)"/>
        <ellipse cx="290" cy="540" rx="230" ry="70" fill="url(#photo-floor)" filter="url(#photo-soften)"/>
        <ellipse cx="275" cy="330" rx="150" ry="200" fill="url(#photo-spot)" filter="url(#photo-soften)"/>
        <ellipse cx="285" cy="520" rx="75" ry="40" fill="url(#photo-spot)" filter="url(#photo-soften)"/>
        <rect x="104" y="102" width="356" height="507" fill="url(#photo-vignette)"/>
      </g>

      <g class="brand-lockup">
        <circle class="brand-mark" cx="140" cy="134" r="6"/>
        <text class="brand-name" x="120" y="158" font-size="15">PLCS</text>
        <text class="brand-name" x="120" y="167" font-size="4.6" textLength="76" lengthAdjust="spacingAndGlyphs">PACIFIC LANTERN CINEMA SHOWCASE</text>
      </g>

      <text class="display-type title-top" x="15" y="87" font-size="78" textLength="522" lengthAdjust="spacingAndGlyphs">PACIFIC</text>
      <text class="display-type title-left" transform="translate(82 707) rotate(-90)" font-size="78" textLength="602" lengthAdjust="spacingAndGlyphs">SHOWCASE</text>
      <text class="display-type title-right" transform="translate(477 102) rotate(90)" font-size="78" textLength="584" lengthAdjust="spacingAndGlyphs">LANTERN CINEMA</text>

      <text class="info-type" x="107" y="659" font-size="42" textLength="157" lengthAdjust="spacingAndGlyphs">AUGUST</text>
      <text class="info-type" x="107" y="692" font-size="22" textLength="152" lengthAdjust="spacingAndGlyphs">23rd . 30th 2019</text>

      <text class="info-type" x="289" y="639" font-size="24" textLength="168" lengthAdjust="spacingAndGlyphs">22ND ANNUAL</text>
      <text class="info-type" x="289" y="662" font-size="24" textLength="110" lengthAdjust="spacingAndGlyphs">FESTIVAL.</text>
      <text class="info-type" x="289" y="692" font-size="17" textLength="168" lengthAdjust="spacingAndGlyphs">WWW.PLCS-SHOWCASE.EXAMPLE</text>
    </svg>
  </article>

  <!-- Variant with circular seal details -->
  <article class="poster poster--seal">
    <svg class="poster-art" viewBox="0 0 560 718" xmlns="http://www.w3.org/2000/svg">
      <defs>
        <path id="seal-ring-annual" d="M309 660 m-30 0 a30 30 0 1 1 60 0 a30 30 0 1 1 -60 0"/>
        <path id="seal-ring-web" d="M411 648 m-33 0 a33 33 0 1 1 66 0 a33 33 0 1 1 -66 0"/>
      </defs>
      <rect class="sheet" width="560" height="718"/>

      <g class="feature-photo" role="img" aria-label="Photograph of a classical plaster bust wearing 3D cinema glasses, lit in magenta and violet against a deep blue studio backdrop" clip-path="url(#photo-frame)">
        <rect x="104" y="102" width="356" height="507" fill="url(#photo-base)"/>
        <ellipse cx="290" cy="540" rx="230" ry="70" fill="url(#photo-floor)" filter="url(#photo-soften)"/>
        <ellipse cx="275" cy="330" rx="150" ry="200" fill="url(#photo-spot)" filter="url(#photo-soften)"/>
        <ellipse cx="285" cy="520" rx="75" ry="40" fill="url(#photo-spot)" filter="url(#photo-soften)"/>
        <rect x="104" y="102" width="356" height="507" fill="url(#photo-vignette)"/>
      </g>

      <g class="brand-lockup">
        <circle class="brand-mark" cx="140" cy="134" r="6"/>
        <text class="brand-name" x="120" y="158" font-size="15">PLCS</text>
        <text class="brand-name" x="120" y="167" font-size="4.6" textLength="76" lengthAdjust="spacingAndGlyphs">PACIFIC LANTERN CINEMA SHOWCASE</text>
      </g>

      <text class="display-type title-top" x="15" y="87" font-size="78" textLength="522" lengthAdjust="spacingAndGlyphs">PACIFIC</text>
      <text class="display-type title-left" transform="translate(82 707) rotate(-90)" font-size="78" textLength="602" lengthAdjust="spacingAndGlyphs">SHOWCASE</text>
      <text class="display-type title-right" transform="translate(477 102) rotate(90)" font-size="78" textLength="584" lengthAdjust="spacingAndGlyphs">LANTERN CINEMA</text>

      <text class="info-type" x="107" y="659" font-size="42" textLength="157" lengthAdjust="spacingAndGlyphs">AUGUST</text>
      <text class="info-type" x="107" y="692" font-size="22" textLength="152" lengthAdjust="spacingAndGlyphs">23rd . 30th 2019</text>

      <text class="seal-type" font-size="10" letter-spacing="1.5">
        <textPath href="#seal-ring-annual">22ND ANNUAL FEST. ·</textPath>
      </text>
      <text class="seal-type" font-size="7.8" letter-spacing="0.6">
        <textPath href="#seal-ring-web">WWW.PLCS-SHOWCASE.EXAMPLE ·</textPath>
      </text>
    </svg>
  </article>

</main>
</body>
</html>
```